Clean book cover design for book about writing a book

Book title: The Turning
Subtitle: 10 Paths to Crafting a Volume of Weight
Name: Mirela K. Dunwoody, The Quill Nestery

This is a book which teaches 10 steps to writing a self-help book. I'm looking for a very clean impactful cover either with no image or just a small simple image of a book, typewriter, laptop, cabin or something very simple. I am attaching the manuscript here if reading it would help you with the cover. The theme of the book is that you can write with joy and ease and your book can just flow out of you if you learn how to clear the blocks between you and your book already written. Sort of a new agey stance on book writing.

The book should generally match the branding on my website. Www.TheQuillNestery.example.

I have photos of myself attached which I'd like used for the back cover with an "about the author section of maybe 50 words.

The project is for the full back cover and spine as well as the front cover (see press Forge template attached) but to win the contest you can just design the front cover and then I'll give the winner the template for the full design with the back cover copy. Or you can design the full cover using the template and you can use Loren ipsum text if you need to.

My clients are very upmarket and the themes of my business revolve around nuturing and incubating ideas and authors. Very feminine creation energy.

For colors see The Turning Press (TH) wax seals and the background fades. I don't want my logo on the cover but I am attaching it here so you get a feel for the branding. The logo is in the LOBSTER font and you can see how we do the grey with the rainbow shadow.

Here are some covers I like:

http://www.bookmarto.example/Pen-Volume-Fast-Stage---Stage/dp/071302488Q
http://www.bookmarto.example/Sketching-Their-Tale-Chart-Triumph/dp/0865713511
http://www.bookmarto.example/Be-Scribe-Seeking-Poet-Guide-ebook/dp/C11G8V9PL7
http://www.bookmarto.example/Strayfolk-Tale-Triumph-Rupert-Hallowmere/dp/0427128041
Updates

I have revised my brief to include some picture and images that will help you create the cover. I have also included some of my favorite covers to give you more of a sense of what I'm going for. And I have included the manuscript in case it would help you to skim through it in order to get a sense of the reader and the book. I think if you look at my revised brief it will make it easier to create a submission. Thanks!

Target Market(s)

Women 40-60 who run small businesses as life coaches or other healing jobs (therapy, reiki, light work) they have a spiritual/new age bent.

Industry/Entity Type

Business

Font styles to use
Serif
Other font styles liked:
• Lobster (not required... just a suggestion since it's my logo font)

Requirements
Must have
• Name and title easy to read in 1" x 1" thumb nail
Nice to have
• Fantastic type face treatment.

Match the look and feel of my website.
Should not have
• Busy images. With one simple image or just designed with colors and typeface treatment

```html
<!DOCTYPE html>
<html lang="en">
<head>
<meta charset="utf-8">
<title>The Turning – Full Cover</title>
<link href="https://fonts.googleapis.com/css2?family=Federo&family=Oswald:wght@400;500;600;700&family=Open+Sans:wght@800&display=swap" rel="stylesheet">
<style>
  :root{
    --bg-cool:#a9bbdf;
    --bg-mid:#c6acd6;
    --bg-warm:#e496bf;
    --panel-top:#c9d8f0;
    --panel-bottom:#e6c8e2;
    --ink:#0d0d0d;
    --paper:#ffffff;
    --accent-red:#e41a1a;
    --portrait-a:#e6dcd2;
    --portrait-b:#3a2c33;
    --seal:#b45aa8;
    --imprint-grey:#4a4a55;
  }
  html,body{margin:0;padding:0;overflow:hidden;}
  body{width:1200px;height:877px;}
  .cover{
    position:relative;width:1200px;height:877px;overflow:hidden;
    background:linear-gradient(115deg,var(--bg-cool) 0%,var(--bg-mid) 50%,var(--bg-warm) 100%);
    font-family:"Oswald",sans-serif;color:var(--ink);
  }
  .back-panel{
    position:absolute;left:27px;top:27px;width:541px;height:651px;
    background:linear-gradient(170deg,var(--panel-top) 0%,#d8d3ec 55%,var(--panel-bottom) 100%);
  }
  .back-title{margin:0;position:absolute;left:0;top:0;width:100%;height:90px;text-align:center;font-family:"Federo",sans-serif;font-weight:400;}
  .back-title .the{position:absolute;left:0;right:0;top:14px;font-size:27px;line-height:1;}
  .back-title .main{position:absolute;left:0;right:0;top:34px;font-size:50px;line-height:1;letter-spacing:1px;}
  .back-rule{position:absolute;left:22px;top:95px;width:498px;height:4px;background:var(--paper);}
  .back-copy{
    position:absolute;left:8px;top:118px;width:526px;
    font-size:13.4px;line-height:17.8px;font-weight:500;text-align:center;
  }
  .back-copy p{margin:0;}
  .back-copy .tail{padding-left:180px;}
  .author-photo{
    position:absolute;left:0;top:414px;width:293px;height:237px;
    background:radial-gradient(ellipse at 45% 40%,var(--portrait-a) 0%,#b79a88 40%,var(--portrait-b) 85%);
  }
  .barcode-box{position:absolute;left:350px;top:696px;width:209px;height:152px;background:var(--paper);}
  .imprint-mark{
    position:absolute;left:69px;top:786px;
    font-family:"Oswald",sans-serif;font-weight:500;font-size:28px;line-height:1.2;color:var(--imprint-grey);
  }
  .spine{position:absolute;left:572px;top:0;width:72px;height:877px;}
  .spine svg,.front svg{display:block;}
  .front{position:absolute;left:660px;top:0;width:540px;height:877px;}
  .book-image{
    position:absolute;left:16px;top:554px;width:503px;height:194px;
    background:linear-gradient(180deg,#fbf8fb 0%,#efe7f0 100%);
    border-radius:8px 8px 4px 4px;
  }
</style>
</head>
<body>
<main class="cover">

  <section class="back-panel">
    <h2 class="back-title"><span class="the">The</span><span class="main">Turning</span></h2>
    <div class="back-rule"></div>
    <div class="back-copy">
      <p>The TURNING Process is detailed – but it's simple, and proven. It breaks down each of the elements that every book that makes a difference does wells, and as you work through this book, you'll see exactly, step-by-step, how you can do it too. If you follow this process, you WILL absolutely end up with a book that matters.</p>
      <p>So here's one last thing I'd like you to do now, before delving deeper. It's a pretty easy exercise, but it's important, too. Take a moment and literally imagine your completed book in your hands right now. Don't worry about the topic of the book, or the style, or anything really – except how the book makes you feel. When you hold that book in your hands, in your mind's eye, see if you can find one word that crystallizes what your book needs to be in the world for you. What's your intention for your book?</p>
      <p>Did you get the word? Great! Once you've got it, I'd like you to write it in some beautiful calligraphy, or use a special font and color and print it out. This is going to be the first building block of your creativity temple.</p>
      <p class="tail">More on that in chapter 6, but for now –<br>just claim your word and give it a place of<br>honor in your office (or wherever you write).</p>
    </div>
    <div class="author-photo" role="img" aria-label="Portrait photograph of the author"></div>
  </section>

  <div class="barcode-box"></div>
  <div class="imprint-mark">The Quill Nestery</div>

  <section class="spine">
    <svg width="72" height="877" viewBox="0 0 72 877">
      <text transform="translate(22,41) rotate(90)" font-family="Federo, sans-serif" fill="#0d0d0d" textLength="389" lengthAdjust="spacingAndGlyphs"><tspan font-size="28">The </tspan><tspan font-size="44">Turning</tspan></text>
      <text transform="translate(22,539) rotate(90)" font-family="Oswald, sans-serif" font-weight="700" font-size="40" fill="#0d0d0d" textLength="302" lengthAdjust="spacingAndGlyphs">Mirela K. Dunwoody</text>
    </svg>
  </section>

  <section class="front">
    <svg width="540" height="877" viewBox="0 0 540 877">
      <defs>
        <filter id="lift" x="-10%" y="-10%" width="120%" height="140%">
          <feDropShadow dx="2" dy="3" stdDeviation="2" flood-color="#000" flood-opacity="0.55"/>
        </filter>
      </defs>
      <text class="title-the" x="222" y="100" font-family="Oswald, sans-serif" font-weight="500" font-size="72" fill="#0d0d0d" textLength="123" lengthAdjust="spacingAndGlyphs">The</text>
      <text class="title-main" x="30" y="228" font-family="Oswald, sans-serif" font-weight="500" font-size="155" fill="#0d0d0d" textLength="486" lengthAdjust="spacingAndGlyphs">Turning</text>
      <rect x="24" y="274" width="491" height="5" fill="#0d0d0d"/>
      <g transform="translate(50,535) skewX(-10)">
        <text x="0" y="0" font-family="Oswald, sans-serif" font-weight="400" font-size="245" fill="#e41a1a" textLength="95" lengthAdjust="spacingAndGlyphs">10</text>
      </g>
      <g font-family="Open Sans, sans-serif" font-weight="800" fill="#ffffff" filter="url(#lift)">
        <text x="192" y="368" font-size="60" textLength="318" lengthAdjust="spacingAndGlyphs">Paths to</text>
        <text x="190" y="430" font-size="60" textLength="300" lengthAdjust="spacingAndGlyphs">Crafting</text>
        <text x="181" y="496" font-size="58" textLength="300" lengthAdjust="spacingAndGlyphs">a Volume</text>
        <text x="179" y="536" font-size="36" textLength="308" lengthAdjust="spacingAndGlyphs">of Weight</text>
      </g>
      <circle cx="40" cy="790" r="26" fill="#b45aa8"/>
      <text x="74" y="801" font-family="Oswald, sans-serif" font-weight="700" font-size="30" fill="#0d0d0d">TH</text>
      <text x="121" y="815" font-family="Oswald, sans-serif" font-weight="700" font-size="52" fill="#0d0d0d" textLength="361" lengthAdjust="spacingAndGlyphs">Mirela K. Dunwoody</text>
    </svg>
    <div class="book-image" role="img" aria-label="Simple line illustration of an open book"></div>
  </section>

</main>
</body>
</html>
```